Heritage Depot Business Cards

Require a business card design. <br/><br/>Needs to include logo (either round or long version) plus these details:<br/>Maya Corvell<br/>Heritage Depot<br/>maya@brightmarttrade.com.au<br/>02 6418 7395<br/>PO Box Glenfarrow NSW 2791<br/>www.heritagedepot.com.au<br/><br/>I need in an editable format so that I can create for multiple staff members. <br/><br/>

Target Market(s)

We are an online store selling renovation products to home owners are builders. Looking for a classic classy design.

Industry/Entity Type

Home And Garden

Contact Information for Business Card

Maya Corvell
Heritage Depot
maya@brightmarttrade.com.au
02 6418 7395
PO Box Glenfarrow NSW 2791
www.heritagedepot.com.au

Colors

Designer to choose colors to be used in the design.

Requirements
Must have
• Must include Logo.

```html
<!DOCTYPE html>
<html lang="en">
<head>
<meta charset="utf-8">
<title>Heritage Depot Business Cards</title>
<link href="https://fonts.googleapis.com/css2?family=Roboto:wght@400;500;700&display=swap" rel="stylesheet">
<style>
  :root {
    --backdrop: #5a5a5a;
    --card: #231f20;
    --ink: #f2f2f2;
    --accent: #4f7d6c;
  }
  * { margin: 0; padding: 0; box-sizing: border-box; }
  html, body { width: 1200px; height: 1021px; overflow: hidden; }
  body {
    background: var(--backdrop);
    font-family: "Roboto", Arial, sans-serif;
    color: var(--ink);
    position: relative;
  }
  .card {
    position: absolute;
    left: 250px;
    width: 700px;
    height: 400px;
    background: var(--card);
    border-radius: 3px;
    box-shadow: 0 14px 30px rgba(0,0,0,0.35);
  }
  .card--front { top: 70px; }
  .card--back { top: 540px; }

  .wordmark {
    font-family: "Roboto", Arial, sans-serif;
    font-weight: 400;
    color: var(--ink);
    display: flex;
    align-items: center;
    gap: 16px;
  }
  .card--front .wordmark {
    position: absolute;
    inset: 0;
    justify-content: center;
    font-size: 44px;
  }
  .wordmark__dot {
    width: 22px; height: 22px;
    border: 2px solid var(--ink);
    border-radius: 50%;
    flex: none;
  }
  .card--back .wordmark {
    position: absolute;
    left: 40px;
    top: 60px;
    font-size: 36px;
  }

  .person {
    position: absolute;
    right: 52px;
    top: 140px;
    text-align: right;
  }
  .person__name {
    font-weight: 700;
    font-size: 21px;
    letter-spacing: 1px;
    color: var(--accent);
    text-transform: uppercase;
  }
  .person__role {
    font-size: 15px;
    letter-spacing: 0.5px;
    text-transform: uppercase;
    margin-top: 2px;
  }

  .contact {
    position: absolute;
    right: 52px;
    bottom: 38px;
    text-align: right;
    font-size: 17px;
    line-height: 23px;
  }
  .contact__address { margin-bottom: 10px; }
  .contact__line {
    display: flex;
    justify-content: flex-end;
    align-items: center;
    gap: 10px;
  }
  .contact__icon { width: 16px; height: 16px; flex: none; }
</style>
</head>
<body>

  <section class="card card--front" aria-label="Card front">
    <div class="wordmark"><span class="wordmark__dot"></span><span>Heritage Depot</span></div>
  </section>

  <section class="card card--back" aria-label="Card back">
    <div class="wordmark"><span class="wordmark__dot"></span><span>Heritage Depot</span></div>

    <div class="person">
      <p class="person__name">Maya Corvell</p>
      <p class="person__role">Owner</p>
    </div>

    <div class="contact">
      <p class="contact__address">PO Box Glenfarrow<br>NSW 2791</p>
      <p class="contact__line">02 6418 7395
        <svg class="contact__icon" viewBox="0 0 16 16" aria-hidden="true"><path d="M4 1.5l2.2 3-1.3 1.6c.8 1.9 2.4 3.5 4.3 4.3l1.6-1.3 3 2.2-1.2 2.4C7 13.5 2.5 9 1.6 2.7z" fill="var(--accent)"/></svg>
      </p>
      <p class="contact__line">maya@brightmarttrade.com.au
        <svg class="contact__icon" viewBox="0 0 16 16" aria-hidden="true"><rect x="1.5" y="3.5" width="13" height="9" fill="none" stroke="var(--accent)" stroke-width="1.4"/><path d="M1.5 3.5L8 9l6.5-5.5" fill="none" stroke="var(--accent)" stroke-width="1.4"/></svg>
      </p>
      <p class="contact__line">www.heritagedepot.com.au
        <svg class="contact__icon" viewBox="0 0 16 16" aria-hidden="true"><g fill="none" stroke="var(--accent)" stroke-width="1.3"><circle cx="8" cy="8" r="6.5"/><ellipse cx="8" cy="8" rx="2.8" ry="6.5"/><path d="M1.5 8h13M2.5 4.8h11M2.5 11.2h11"/></g></svg>
      </p>
    </div>
  </section>

</body>
</html>
```